Camp Thornbrook 2021 Magazine Design

We are for someone to design our annual magazine/newsletter. This is a print newsletter that is a total of 20 pages. It will need to be designed in a way that is easy to share with our printers. The designer will need to be someone who is creative and easy to work with.
For those interested in this project we ask that you design 4 to 6 pages for us to view. Once we select the designer we will want the rest created in a two-week time span. For those submitting a bid please include front cover, theme & dates, mission & vision, and Lend a Hand Forward.

This link will provide the layout of the newsletter https://files.pelmarsh.example/doc/7qTzR2kLpW9xVbN4cHsYd/view.

This link will provide you with the pictures that are needed and a few documents https://files.pelmarsh.example/folder/3hGvK8mQxZ5rLtP1wNcBj/view

Details:
20 pages long (including covers)
8.5 x 11

Please message me if you need any further details.

Target Market(s)

Our alumni base. Covers all ages

Requirements
Must have
• Spelled out in document
Nice to have
• Spelled out in document
Should not have
• Spelled out in document

```html
<!DOCTYPE html>
<html lang="en">
<head>
<meta charset="utf-8">
<title>Resurrection 2021 – Camp Thornbrook</title>
<link href="https://fonts.googleapis.com/css2?family=Poppins:wght@600&family=Roboto+Condensed:ital,wght@0,400;0,700;1,400&family=Noto+Serif:wght@400;700&display=swap" rel="stylesheet">
<style>
  :root{
    --sky-top:#5d6063;
    --sky-mid:#9a9fa2;
    --mist:#cfd5d8;
    --forest:#5a4a3c;
    --panel:rgba(52,55,58,0.72);
    --white:#ffffff;
    --green:#b5d98a;
    --bullet:#8cc35a;
    --navy:#2b2d4f;
    --teal:#82c5b8;
    --rule:rgba(255,255,255,0.35);
  }
  *{margin:0;padding:0;box-sizing:border-box}
  html,body{width:927px;height:1200px;overflow:hidden}
  body{position:relative;font-family:"Noto Serif",serif;color:var(--white)}
  .page{position:relative;width:927px;height:1200px;overflow:hidden}
  .backdrop{
    position:absolute;inset:0;
    background:
      radial-gradient(ellipse 70% 20% at 75% 78%, rgba(120,80,50,0.55), transparent 70%),
      radial-gradient(ellipse 80% 22% at 20% 70%, rgba(50,55,55,0.5), transparent 70%),
      linear-gradient(180deg,var(--sky-top) 0%,var(--sky-mid) 35%,#7c8184 60%,var(--mist) 88%,#d6dbdd 100%);
  }
  .panel{
    position:absolute;left:113px;top:167px;width:698px;height:720px;
    border-radius:18px 18px 0 0;
    background:linear-gradient(180deg,var(--panel) 0%,var(--panel) 70%,rgba(52,55,58,0) 100%);
  }
  .title{
    position:absolute;left:151px;top:238px;
    font-family:"Poppins",sans-serif;font-weight:600;font-size:87px;letter-spacing:1px;line-height:1;
    color:transparent;-webkit-text-stroke:2px var(--white);
    background:repeating-linear-gradient(0deg,rgba(255,255,255,0.85) 0 1px,transparent 1px 4px);
    -webkit-background-clip:text;background-clip:text;
  }
  .year{
    position:absolute;left:150px;top:328px;
    font-family:"Poppins",sans-serif;font-weight:600;font-size:100px;line-height:1;
    color:transparent;-webkit-text-stroke:2.5px var(--green);
    background:repeating-linear-gradient(0deg,rgba(181,217,138,0.9) 0 1px,transparent 1px 4px);
    -webkit-background-clip:text;background-clip:text;
  }
  .verse{
    position:absolute;right:160px;top:340px;width:360px;text-align:right;
    font-family:"Roboto Condensed",sans-serif;font-size:16px;line-height:22px;
  }
  .verse cite{display:block;color:var(--green);font-style:italic}
  .info-heading{
    position:absolute;left:165px;top:495px;width:322px;height:29px;padding-left:20px;
    background:var(--navy);
    font-family:"Roboto Condensed",sans-serif;font-weight:700;font-size:18px;line-height:29px;
  }
  .info-list{position:absolute;left:113px;top:530px;width:580px;list-style:none}
  .info-list li{
    position:relative;height:35.3px;padding-left:72px;padding-top:4px;
    font-size:15.5px;border-bottom:1px dotted var(--rule);
  }
  .info-list li::before{
    content:"";position:absolute;left:54px;top:13px;width:7px;height:7px;border-radius:50%;background:var(--bullet);
  }
  .info-list li::after{
    content:"";position:absolute;right:-2px;bottom:-3px;width:4px;height:4px;border-radius:50%;border:1px solid var(--rule);
  }
  .info-list strong{font-weight:700}
  .folio{
    position:absolute;left:16px;top:1152px;width:18px;height:24px;background:var(--teal);
    font-family:"Roboto Condensed",sans-serif;font-size:13px;color:#1d2a28;text-align:center;line-height:26px;
  }
  .footer-band{position:absolute;left:0;bottom:0;width:927px;height:24px;background:var(--teal)}
</style>
</head>
<body>
<main class="page">
  <div class="backdrop" role="img" aria-label="Misty mountain landscape under grey clouds with a snowy peak and an autumn pine forest rising through fog"></div>
  <section class="panel" aria-hidden="true"></section>
  <h1 class="title">RESURRECTION</h1>
  <div class="year">2021</div>
  <blockquote class="verse">
    “ Jesus said to her, “I am the resurrection and the life. The one who believes in me will live, even though they die;””
    <cite>John 11:25</cite>
  </blockquote>
  <h2 class="info-heading">Registration and other information:</h2>
  <ul class="info-list">
    <li>Registration begins on <strong>January 1, 2021</strong></li>
    <li>Register online at <strong>campthornbrook.org</strong></li>
    <li>Super Early Bird Discount <strong>($20)</strong> if registered before <strong>April 1st</strong></li>
    <li>Early Bird Discount <strong>($10)</strong> if registered in the month of <strong>April</strong></li>
  </ul>
  <div class="folio">6</div>
  <div class="footer-band"></div>
</main>
</body>
</html>
```